I am looking for business cards and letterhead

I want a high-level look for CEO's who want a concierge level leadership consultant and organization development strategist

This needs to go with my brand: simple, elegant, clean. Please improve on this design while using these fonts and colors

Here is my website: CorinneValdez.com

```html
<!DOCTYPE html>
<html lang="en">
<head>
<meta charset="utf-8">
<title>Corinne Valdez — Stationery</title>
<link rel="stylesheet" href="https://fonts.googleapis.com/css2?family=Public+Sans:wght@400;500;700&display=swap">
<style>
  :root {
    --backdrop: #d4d5d8;
    --paper: #ffffff;
    --card-tint: #f2f9fc;
    --navy: #0b2a3e;
    --teal: #5195a0;
    --gold: #b8935a;
    --ink: #2b2f33;
    --photo-light: #e9eef0;
    --photo-dark: #1f4a3c;
  }
  * { box-sizing: border-box; margin: 0; padding: 0; }
  html, body {
    width: 1200px; height: 941px; overflow: hidden;
    background: var(--backdrop);
    font-family: "Public Sans", Arial, sans-serif;
  }
  .canvas { position: relative; width: 1200px; height: 941px; }

  /* Letterhead */
  .letterhead {
    position: absolute; left: 98px; top: 70px; width: 613px; height: 793px;
    background: var(--paper);
    box-shadow: 0 0 12px rgba(0,0,0,.35);
  }
  .letterhead .brand {
    position: absolute; left: 40px; top: 48px;
    display: flex; align-items: center; gap: 10px;
  }
  .brand-dot { width: 22px; height: 22px; border-radius: 50%; background: var(--gold); flex: none; }
  .brand-name { font-weight: 700; color: var(--navy); font-size: 17px; letter-spacing: .02em; }
  .letterhead .contact {
    position: absolute; left: 400px; top: 38px;
    list-style: none; font-size: 11px; color: var(--ink);
  }
  .contact li { display: flex; align-items: center; gap: 7px; height: 17.6px; }
  .contact svg { width: 9px; height: 9px; fill: var(--ink); flex: none; }
  .letterhead .rule-thick {
    position: absolute; left: 0; right: 0; top: 120px; height: 3px; background: var(--navy);
  }
  .letterhead .rule-thin {
    position: absolute; left: 0; right: 0; top: 125px; height: 1px; background: var(--navy);
  }

  /* Business card front */
  .card { position: absolute; left: 745px; width: 356px; height: 219px; box-shadow: 0 0 8px rgba(0,0,0,.3); overflow: hidden; }
  .card-front { top: 242px; background: var(--card-tint); }
  .card-front .brand { position: absolute; left: 18px; top: 44px; display: flex; align-items: center; gap: 7px; }
  .card-front .brand-dot { width: 16px; height: 16px; }
  .card-front .brand-name { font-size: 12px; }
  .card-front .name {
    position: absolute; left: 19px; top: 122px;
    font-weight: 700; font-size: 16px; color: var(--navy);
  }
  .card-front .role {
    position: absolute; left: 19px; top: 142px;
    font-size: 10.5px; color: var(--navy);
    display: flex; align-items: center; gap: 4px;
  }
  .role::after { content: ""; width: 50px; height: 1px; background: var(--teal); }
  .card-front .contact {
    position: absolute; left: 19px; top: 167px; list-style: none;
    font-size: 8px; color: var(--ink);
  }
  .card-front .contact li { height: 13.4px; gap: 5px; }
  .card-front .contact svg { width: 7px; height: 7px; }
  .portrait {
    position: absolute; left: 218px; top: 58px; width: 138px; height: 154px;
    background: linear-gradient(180deg, var(--photo-light) 0%, #9a6b52 45%, var(--photo-dark) 100%);
  }
  .card-front .band { position: absolute; left: 0; right: 0; bottom: 0; height: 7px; background: var(--teal); }

  /* Business card back */
  .card-back { top: 484px; background: var(--navy); display: flex; align-items: center; justify-content: center; gap: 10px; }
  .card-back .brand-dot { width: 20px; height: 20px; }
  .card-back .brand-name { color: var(--gold); font-size: 17px; }
</style>
</head>
<body>
<main class="canvas">
  <svg width="0" height="0" style="position:absolute">
    <defs>
      <symbol id="icon-mail" viewBox="0 0 16 16"><path d="M1 3h14v10H1z M1 3l7 6 7-6" /><path d="M1.5 3.5 8 8.8l6.5-5.3v.9L8 9.9 1.5 4.4z" fill="#fff"/></symbol>
      <symbol id="icon-phone" viewBox="0 0 16 16"><path d="M3.6 1.2l2.3 2.9-1.3 1.9c.9 2 2.5 3.6 4.5 4.5l1.9-1.3 2.9 2.3-1.4 2.6C6.8 14 2 9.2 1 3.9z"/></symbol>
      <symbol id="icon-web" viewBox="0 0 16 16"><path d="M8 1a7 7 0 1 0 0 14A7 7 0 0 0 8 1zm0 1.3c.8.9 1.4 2.1 1.7 3.4H6.3C6.6 4.4 7.2 3.2 8 2.3zM2.5 9.7a5.8 5.8 0 0 1 0-3.4h2.6a11 11 0 0 0 0 3.4zm.5 1.3h2.3c.3 1.1.7 2 1.2 2.8A5.7 5.7 0 0 1 3 11zm2.3-6H3a5.7 5.7 0 0 1 3.5-2.8C6 3 5.6 3.9 5.3 5zM8 13.7c-.8-.9-1.4-2.1-1.7-3.4h3.4c-.3 1.3-.9 2.5-1.7 3.4zm2-4.7H6a9.6 9.6 0 0 1 0-2.6h4a9.6 9.6 0 0 1 0 2.6zm-.5 4.8c.5-.8.9-1.7 1.2-2.8H13a5.7 5.7 0 0 1-3.5 2.8zm1.4-4.1a11 11 0 0 0 0-3.4h2.6a5.8 5.8 0 0 1 0 3.4zM10.7 5c-.3-1.1-.7-2-1.2-2.8A5.7 5.7 0 0 1 13 5z"/></symbol>
    </defs>
  </svg>

  <section class="letterhead" aria-label="Letterhead">
    <div class="brand"><span class="brand-dot"></span><span class="brand-name">Corinne Valdez</span></div>
    <ul class="contact">
      <li><svg><use href="#icon-mail"/></svg>Valdez@corinnevaldez.com</li>
      <li><svg><use href="#icon-phone"/></svg>555 014 2368</li>
      <li><svg><use href="#icon-web"/></svg>www.corinnevaldez.com</li>
    </ul>
    <div class="rule-thick"></div>
    <div class="rule-thin"></div>
  </section>

  <section class="card card-front" aria-label="Business card front">
    <div class="brand"><span class="brand-dot"></span><span class="brand-name">Corinne Valdez</span></div>
    <h1 class="name">Corinne Valdez</h1>
    <p class="role">Business Coach</p>
    <ul class="contact">
      <li><svg><use href="#icon-mail"/></svg>Valdez@corinnevaldez.com</li>
      <li><svg><use href="#icon-phone"/></svg>555 014 2368</li>
      <li><svg><use href="#icon-web"/></svg>www.corinnevaldez.com</li>
    </ul>
    <div class="portrait" role="img" aria-label="Portrait photo of the coach in a dark green blazer"></div>
    <div class="band"></div>
  </section>

  <section class="card card-back" aria-label="Business card back">
    <span class="brand-dot"></span><span class="brand-name">Corinne Valdez</span>
  </section>
</main>
</body>
</html>
```